Jetzt starten So funktioniert'sAuf die Visitenkarte soll ein Logo bzw. eine Grafik dargestellt werden, welche ebenfalls auf der Website und dem Flyer genutzt werden soll wird es hier als Logo bezeichnet. Die Grafik soll ein Labyrinth und eine Person in einer scheinbar aussichtsloser Lage darstellen mit der Frage „KOMPASS gefä..
16Stein, Weg, Füße, Baby o. Kind....Sonne... Vielleicht fällt Ihnen auch etwas besseres ein. Evtl. ein Slogan wie z. B. -Kinderbetreuung mit ❤️ - Hier steht das Kind im Mittelpunkt. -Jedes Kind ist einzigartig? Oder - „Hilf mir es selbst zu tun“ aber vielleicht anders formuliert. (..
40Es müssen für zwei Geschäfte Visitenkarten, Briefpapier (A4) und Kassenkassenbelege (A6) erstellt werden. Logo und Typo im Anhang. Ein Farbkonzept besteht noch nicht. Die Idee geht in Richtung Bordeaux-Rot. Generell: (1) Sieht erstmal nach viel Beschreibung aus, bitte nicht entmutigen lass..
118Schlichtes aber direkt erkennbares Design. Koch dir Kraft , Gesundheit und Ernährungsberatung ( gut lesbar , elegant) Miriam Holtz-Ebersbach ( nicht so groß ) Grau ; Grün Töne und gerne etwas rosa Infos wie Adresse und E-Mail vielleicht in jeweilige Blöcke am unteren Rand
30Wir benötigen, passend zu unserem neuen Logo, Geschäftspapier, Visitenkarten und eine Vorlage für eine PowerPoint Präsentation (Hintergrunds-Seite)

```html
<!DOCTYPE html>
<html lang="de">
<head>
<meta charset="utf-8">
<title>Lukas Marten – Briefpapier</title>
<link href="https://fonts.googleapis.com/css2?family=Tinos:wght@400&display=swap" rel="stylesheet">
<style>
  :root {
    --band: #d6a596;
    --panel: #c9675d;
    --wine: #b0182f;
    --ink: #8a2c2c;
    --footer-ink: #6e2424;
    --paper: #ffffff;
    --white: #ffffff;
  }
  html, body {
    margin: 0;
    padding: 0;
    overflow: hidden;
  }
  body {
    width: 922px;
    height: 1200px;
    background: var(--paper);
    font-family: "Tinos", "Times New Roman", serif;
  }
  .letterhead {
    position: relative;
    width: 922px;
    height: 1200px;
    background: var(--paper);
    overflow: hidden;
  }
  .top-band {
    position: absolute;
    left: 0; top: 0;
    width: 922px;
    height: 107px;
    background: var(--band);
  }
  .brand-panel {
    position: absolute;
    left: 484px; top: 67px;
    width: 438px;
    height: 95px;
    background: var(--panel);
  }
  .brand-name {
    position: absolute;
    left: 30px; top: 12px;
    width: 396px;
    height: 44px;
    background: var(--wine);
    color: var(--white);
    font-size: 38px;
    line-height: 46px;
    letter-spacing: 1px;
    padding-left: 14px;
    box-sizing: border-box;
    margin: 0;
    font-weight: 400;
  }
  .brand-services {
    position: absolute;
    left: 32px; top: 62px;
    margin: 0;
    color: var(--white);
    font-size: 19px;
    line-height: 24px;
    white-space: nowrap;
  }
  .sender-line {
    position: absolute;
    left: 92px; top: 228px;
    margin: 0;
    color: var(--ink);
    font-size: 13px;
  }
  .footer-band {
    position: absolute;
    left: 0; top: 1089px;
    width: 922px;
    height: 111px;
    background: var(--band);
    color: var(--footer-ink);
    font-size: 13px;
  }
  .footer-contact {
    position: absolute;
    left: 92px; top: 20px;
    margin: 0;
  }
  .footer-bank {
    position: absolute;
    left: 92px; top: 45px;
    margin: 0;
    line-height: 16px;
  }
</style>
</head>
<body>
  <main class="letterhead">
    <header class="top-band"></header>
    <div class="brand-panel">
      <h1 class="brand-name">LUKAS MARTEN</h1>
      <p class="brand-services">Korrektorat • Textredaktion • Ghostwriting</p>
    </div>

    <p class="sender-line">Lukas Marten Holunderweg 14, 25436 Moorrege</p>

    <footer class="footer-band">
      <p class="footer-contact">Lukas Marten Holunderweg 14, 25436 Moorrege Tel. (0 41 22) 4 70 19 28 • l.marten@beispielpost.de</p>
      <p class="footer-bank">
        Kto.-Nr. 61 284 300, Musterbank Nord eG, BLZ 200 505 99<br>
        IBAN DE12200505990061284300, BIC MUSTDEH1NRD<br>
        USt-IdNr. DE987654321
      </p>
    </footer>
  </main>
</body>
</html>
```